Fontenot Bayou Grillhouse (Owners Card)

Need a classy, but modern business card. I have included a promotional card for the steakhouse. I need one for myself (the owner) that is more professional.

Target Market(s)

General Public

Industry/Entity Type

Food service

Contact Information for Business Card

Name, business address, phone number, email, logo

Font styles to use
Serif
Sans Serif
Decorative
Script

Requirements
Must have
• My name (Darvel Pruitt), business address (327 Oakmere Street), phone number (510) 493-2615, email (Dpruittkr4@mailvane.example. On the back of the card: Psalms 27 1 The LORD is my light and my salvation— whom shall I fear? The LORD is the stronghold of my life— of whom shall I be afraid? 2 When the wicked advance against me to devour me, it is my enemies and my foes who will stumble and fall. 3 Though an army besiege me, my heart will not fear; though war break out against me, even then I will be confident.
Nice to have
• Something that’s bold, but modern and professional.

```html
<!DOCTYPE html>
<html lang="en">
<head>
<meta charset="utf-8">
<title>Darvel Pruitt – Owner's Card</title>
<link rel="stylesheet" href="https://fonts.googleapis.com/css2?family=Playfair+Display:wght@400;700&family=Montserrat:wght@400;500&family=Dancing+Script:wght@500&display=swap">
<style>
  :root {
    --backdrop: #1c1c1c;
    --card-black: #141414;
    --card-black-edge: #202020;
    --card-white: #f6f6f4;
    --band: #141414;
    --ink-light: #e6e6e6;
    --ink-muted: #9a9a9a;
    --ink-dark: #2a2a2a;
    --rule: #6a6a6a;
    --ornament: #3a3a3a;
  }
  * { box-sizing: border-box; margin: 0; padding: 0; }
  html, body { width: 1200px; height: 852px; overflow: hidden; }
  body {
    background: var(--backdrop);
    position: relative;
  }
  .card {
    position: absolute;
    top: 277px;
    width: 520px;
    height: 298px;
    border-radius: 24px;
    overflow: hidden;
  }
  /* Back: scripture side */
  .card-back {
    left: 50px;
    background: linear-gradient(160deg, var(--card-black-edge), var(--card-black));
    color: var(--ink-light);
    font-family: "Playfair Display", Georgia, serif;
    padding: 34px 40px;
  }
  .card-back .rule {
    width: 330px;
    height: 1px;
    background: var(--rule);
  }
  .scripture-title {
    font-weight: 700;
    font-size: 17px;
    margin: 48px 0 8px;
  }
  .scripture-title + .rule { margin-bottom: 12px; width: 360px; }
  .verse {
    font-size: 11.5px;
    line-height: 1.45;
    margin-bottom: 9px;
    max-width: 420px;
  }
  .ornament {
    position: absolute;
    top: 24px;
    right: 30px;
    width: 60px;
    height: 120px;
    border-radius: 30px;
    background: radial-gradient(circle at 40% 35%, #4a4a4a, var(--ornament) 60%, var(--card-black));
  }
  /* Front: contact side */
  .card-front {
    left: 630px;
    background: var(--card-white);
    font-family: "Montserrat", Arial, sans-serif;
  }
  .name-band {
    position: absolute;
    top: 100px;
    left: 0;
    width: 100%;
    height: 62px;
    background: var(--band);
    display: flex;
    align-items: center;
    justify-content: center;
  }
  .owner-name {
    font-family: "Dancing Script", cursive;
    font-weight: 500;
    font-size: 34px;
    color: var(--card-white);
  }
  .contact {
    position: absolute;
    top: 174px;
    left: 0;
    width: 100%;
    text-align: center;
    color: var(--ink-dark);
    font-size: 12px;
    line-height: 1.7;
  }
  .contact-row { display: flex; justify-content: center; gap: 18px; }
  .contact-item { display: inline-flex; align-items: center; gap: 6px; }
  .contact-item svg { width: 12px; height: 12px; fill: var(--ink-dark); }
</style>
</head>
<body>

<section class="card card-back" aria-label="Card back with Psalm 27:1–3">
  <div class="ornament" role="img" aria-label="Embossed decorative swirl ornament"></div>
  <div class="rule"></div>
  <h2 class="scripture-title">Psalms 27 (1:3)</h2>
  <div class="rule"></div>
  <p class="verse">The LORD is my light and my salvation— whom shall I fear? The LORD is the stronghold of my life— of whom shall I be afraid?</p>
  <p class="verse">When the wicked advance against me to devour me, it is my enemies and my foes who will stumble and fall.</p>
  <p class="verse">Though an army besiege me, my heart will not fear; though war break out against me, even then I will be confident.</p>
</section>

<section class="card card-front" aria-label="Card front with contact details">
  <div class="name-band">
    <h1 class="owner-name">Darvel Pruitt</h1>
  </div>
  <div class="contact">
    <div class="contact-row">
      <span class="contact-item">
        <svg viewBox="0 0 24 24" aria-hidden="true"><path d="M6.6 10.8a15 15 0 0 0 6.6 6.6l2.2-2.2a1 1 0 0 1 1-.25 11.4 11.4 0 0 0 3.6.57 1 1 0 0 1 1 1V20a1 1 0 0 1-1 1A17 17 0 0 1 3 4a1 1 0 0 1 1-1h3.5a1 1 0 0 1 1 1c0 1.25.2 2.45.57 3.57a1 1 0 0 1-.25 1z"/></svg>
        (510) 493-2615
      </span>
      <span class="contact-item">
        <svg viewBox="0 0 24 24" aria-hidden="true"><path d="M2 5h20v14H2z M2 5l10 8 10-8" fill="none" stroke="#2a2a2a" stroke-width="2"/></svg>
        Dpruittkr4@mailvane.example
      </span>
    </div>
    <div class="contact-row">
      <span class="contact-item">
        <svg viewBox="0 0 24 24" aria-hidden="true"><path d="M12 2a7 7 0 0 0-7 7c0 5 7 13 7 13s7-8 7-13a7 7 0 0 0-7-7zm0 9.5A2.5 2.5 0 1 1 12 6.5a2.5 2.5 0 0 1 0 5z"/></svg>
        327 Oakmere Street, USA
      </span>
    </div>
  </div>
</section>

</body>
</html>
```